Plakate für ein Juwelier Geschäft
Zielgruppe
Juwelier Geschäft mit Gold, Silber, Diamanten und Trauringe. Zielgruppe Schmuck Interessierte, besonders individuelle Trauringberatung mit Konfiguration für junge Paare mit 20 % Rabatt
Aufgabenstellung
2 Bilder: Auf dem ersten Bild Goldschmuck mit Kette, Ring und Ohrringe bei einer jungen Dame und beim zweiten Bild ein junges Paar mit Trauringen. Spruch ist erwünscht. Name, Logo und Adresse vom Laden wird später ergänzt. Bitte kostenlose bzw, lizenzfreie Bilder verwenden. Plakat wird digital benutzt, Auflösung 576 x 408 Pixel, Schrifthöhe 30 Pixel und 50 Pixel

```html
<!DOCTYPE html>
<html lang="de">
<head>
<meta charset="utf-8">
<title>Juwelier Vesta – Trau dich!</title>
<link href="https://fonts.googleapis.com/css2?family=Playfair+Display:wght@400;500;900&family=Open+Sans:wght@400&display=swap" rel="stylesheet">
<style>
  :root {
    --canvas: #f0eeef;
    --poster: #ffffff;
    --ink: #1e1e1e;
    --gold: #d89e36;
    --photo-warm: #f3e4de;
    --photo-cool: #e6e8f0;
    --photo-skin: #e9c9b8;
    --ring-gold: #c9a24a;
    --ring-light: #f1dba0;
  }
  * { margin: 0; padding: 0; box-sizing: border-box; }
  html, body { width: 811px; height: 1200px; overflow: hidden; }
  body { background: var(--canvas); position: relative; }

  .poster {
    position: absolute;
    left: 55px;
    width: 701px;
    height: 497px;
    background: var(--poster);
    overflow: hidden;
  }
  .poster--inline { top: 72px; }
  .poster--stacked { top: 632px; }

  .poster__photo {
    position: absolute;
    left: 340px; top: 0;
    width: 361px; height: 435px;
    background:
      radial-gradient(ellipse 70px 80px at 175px 60px, var(--photo-skin), transparent 75%),
      radial-gradient(ellipse 60px 70px at 300px 40px, var(--photo-skin), transparent 75%),
      linear-gradient(160deg, var(--photo-warm) 0%, var(--photo-cool) 70%);
    -webkit-mask-image: linear-gradient(to right, transparent 0%, #000 40%), linear-gradient(to top, transparent 0%, #000 25%);
    -webkit-mask-composite: source-in;
    mask-image: linear-gradient(to right, transparent 0%, #000 40%), linear-gradient(to top, transparent 0%, #000 25%);
    mask-composite: intersect;
    opacity: 0.85;
  }
  .poster__rings {
    position: absolute;
    left: 506px; top: 339px;
    width: 116px; height: 108px;
    border-radius: 50% 50% 45% 45%;
    background: radial-gradient(ellipse at 40% 40%, var(--ring-light), var(--ring-gold) 60%, rgba(201,162,74,0.15) 100%);
    opacity: 0.8;
  }

  .brand {
    position: absolute;
    left: 42px; top: 44px;
    font-family: "Playfair Display", serif;
    color: var(--ink);
  }
  .brand__name {
    font-size: 30px;
    font-weight: 400;
    line-height: 1;
    letter-spacing: 0.5px;
    text-transform: uppercase;
  }
  .brand__claim {
    margin-top: 6px;
    font-family: "Open Sans", sans-serif;
    font-size: 10.5px;
    letter-spacing: 0.3px;
  }

  .headline {
    position: absolute;
    left: 40px; top: 190px;
    font-family: "Playfair Display", serif;
    font-weight: 500;
    font-size: 66px;
    line-height: 1;
    color: var(--ink);
  }
  .offer {
    position: absolute;
    left: 42px; top: 262px;
    font-family: "Playfair Display", serif;
    font-weight: 900;
    font-size: 54px;
    line-height: 1;
    color: var(--gold);
    letter-spacing: -0.5px;
  }

  .address {
    position: absolute;
    left: 41px;
    font-family: "Open Sans", sans-serif;
    font-size: 26px;
    line-height: 34px;
    color: var(--ink);
  }
  .address--inline { top: 422px; }
  .address--stacked { top: 385px; }
  .address__divider { color: var(--gold); padding: 0 8px; }
</style>
</head>
<body>
  <section class="poster poster--inline">
    <div class="poster__photo" role="img" aria-label="Foto eines jungen Brautpaars in zarter Umarmung, weich ausgeblendet"></div>
    <div class="poster__rings" role="img" aria-label="Zwei goldene Trauringe, ineinander zu einem Herz geformt"></div>
    <div class="brand">
      <div class="brand__name">Juwelier Vesta</div>
      <div class="brand__claim">TRAURINGE | UHREN | SCHMUCK</div>
    </div>
    <h1 class="headline">Trau dich!</h1>
    <p class="offer">20% Rabatt</p>
    <p class="address address--inline">Lindenweg 14<span class="address__divider">|</span>90411 Auenbach</p>
  </section>

  <section class="poster poster--stacked">
    <div class="poster__photo" role="img" aria-label="Foto eines jungen Brautpaars in zarter Umarmung, weich ausgeblendet"></div>
    <div class="poster__rings" role="img" aria-label="Zwei goldene Trauringe, ineinander zu einem Herz geformt"></div>
    <div class="brand">
      <div class="brand__name">Juwelier Vesta</div>
      <div class="brand__claim">TRAURINGE | UHREN | SCHMUCK</div>
    </div>
    <h1 class="headline">Trau dich!</h1>
    <p class="offer">20% Rabatt</p>
    <p class="address address--stacked">Lindenweg 14<br>90411 Auenbach</p>
  </section>
</body>
</html>
```